IRON MARK TRAINING- Shooting Range!!!And virtual shooting range!!!

We are looking to do a clean cut web page for shooting range. We have indoor shooting simulator, retail store that sales accessories and pistols, rifles and shot guns. We are membership based for indoor shooting range Only and virtual shooting is open to public as well as retail store. We also specialize in shooting training classes and CWP classes.
Updates

Thank you for your patience. We are working with a busy travel schedule. We will be making final decisions tomorrow and moving forward with getting this launched. Regards, Howard

Target Market(s)

Public and private entertainment

Industry/Entity Type

Training

Number of Pages Required

5+ page

Font styles to use
Sans Serif

Requirements
Must have
• Clean and easy approach we really like the website our friend has www.pelvornsystems.com please take a look at a lay out. We would like to also add onli member schedule that is available for shooting sections and that they can access and book them selvs.
Nice to have
• White, black, gray or red colors

```html
<!DOCTYPE html>
<html lang="en">
<head>
<meta charset="utf-8">
<title>Iron Mark Training</title>
<link href="https://fonts.googleapis.com/css2?family=Open+Sans:wght@400;600&family=Arimo:wght@400;700&display=swap" rel="stylesheet">
<style>
:root{
  --page-bg:#d9d9d9;
  --white:#ffffff;
  --red:#a30f16;
  --red-bright:#c0141c;
  --nav:#1c1c1c;
  --footer:#1e1e1e;
  --footer-bar:#2b2b2b;
  --gray-btn:#8a8a8a;
  --text:#333333;
  --muted:#8c8c8c;
  --light:#f3f3f3;
}
*{box-sizing:border-box;margin:0;padding:0}
html,body{width:1200px;height:1167px;overflow:hidden}
body{background:var(--page-bg);font-family:"Open Sans",Arial,sans-serif;color:var(--text);position:relative}
.site{position:absolute;left:88px;top:0;width:1008px;height:1167px;background:var(--white)}
.abs{position:absolute}

/* header */
.brand{left:30px;top:18px;display:flex;align-items:center;gap:8px}
.brand-mark{width:40px;height:40px;border-radius:50%;background:var(--red-bright)}
.brand-name{font-size:13px;font-weight:600;color:var(--red-bright);letter-spacing:.5px}
.tagline{right:20px;top:18px;text-align:right}
.tagline h2{font-weight:400;font-size:17px;color:var(--red-bright);letter-spacing:.5px}
.tagline p{font-size:10px;color:var(--muted);line-height:13px;margin-top:6px}

/* nav */
.nav{left:0;top:78px;width:1008px;height:30px;background:var(--nav)}
.nav a{position:absolute;top:0;line-height:30px;font-size:9px;color:#eee;text-decoration:none;text-transform:uppercase}
.nav .register{right:0;width:111px;text-align:center;background:var(--red)}

/* hero */
.hero{left:0;top:108px;width:1008px;height:388px;overflow:hidden}
.hero-photo{position:absolute;inset:0;background:
  radial-gradient(ellipse at 20% 45%,#3e6a8a 0%,#1c3448 35%,transparent 60%),
  radial-gradient(ellipse at 75% 60%,#4a4a48 0%,#2a2a2a 45%,transparent 75%),
  linear-gradient(90deg,#0f1c28 0%,#1b2d3b 40%,#2a2b2b 70%,#1a1a1a 100%)}
.hero-copy{left:85px;top:118px;width:255px;text-align:center}
.hero-copy h1{font-weight:400;font-size:19px;color:var(--red-bright)}
.hero-copy .rule{width:38px;height:1px;background:#ccc;margin:14px auto 16px}
.hero-copy p{font-size:10.5px;line-height:16px;color:#eee}

/* cards */
.card{overflow:hidden;color:#fff;text-align:center}
.card-photo{position:absolute;inset:0}
.card h3{position:absolute;left:0;right:0;white-space:nowrap;font-family:Arimo,Arial,sans-serif;font-weight:400;font-size:21px;line-height:24px;letter-spacing:.3px}
.card p{position:absolute;left:95px;right:95px;font-family:Arimo,Arial,sans-serif;font-size:9.5px;line-height:13px;font-weight:700}
.btns{position:absolute;left:0;right:0;display:flex;justify-content:center}
.btn{display:block;height:25px;line-height:25px;font-family:Arimo,Arial,sans-serif;font-size:8px;text-transform:uppercase;text-align:center;color:#fff;white-space:nowrap}
.btn-red{background:var(--red);width:120px}
.btn-gray{background:var(--gray-btn);width:120px}
.btn-white{background:#fff;color:#333;width:120px}
.btn-outline{border:1px solid #fff;width:118px}

.retail{left:12px;top:514px;width:481px;height:177px}
.retail .card-photo{background:linear-gradient(120deg,#e6e6e6 0%,#9a9a9a 40%,#3a3a3a 75%,#1f1f1f 100%)}
.staff{left:510px;top:514px;width:481px;height:177px}
.staff .card-photo{background:linear-gradient(90deg,#222 0%,#4b4b4b 40%,#6a6158 65%,#8d2a26 90%,#b52a26 100%)}
.tech{left:12px;top:706px;width:481px;height:177px}
.tech .card-photo{background:linear-gradient(90deg,#9a958e 0%,#5c5854 25%,#2a2a2a 55%,#141414 100%)}
.facility{left:510px;top:706px;width:233px;height:177px}
.facility .card-photo{background:linear-gradient(180deg,#3c332b 0%,#8e7b63 50%,#6d5d4b 75%,#2a2623 100%)}
.experience{left:757px;top:706px;width:234px;height:177px}
.experience .card-photo{background:linear-gradient(90deg,#3a3d42 0%,#6e7379 45%,#9aa0a6 70%,#50545a 100%)}

/* newsletter */
.newsletter{left:0;top:902px;width:1008px;height:61px;background:var(--light);border-top:1px solid #ddd}
.newsletter h4{position:absolute;left:214px;top:13px;font-family:Arimo,Arial,sans-serif;font-weight:400;font-size:16px;color:#333}
.newsletter p{position:absolute;left:214px;top:34px;font-size:8px;color:#aaa}
.news-field{position:absolute;left:531px;top:13px;width:358px;height:32px;background:#fff;border:1px solid #ddd}
.news-btn{position:absolute;left:807px;top:17px;width:79px;height:25px;line-height:25px;background:var(--red);color:#fff;font-family:Arimo,Arial,sans-serif;font-size:9px;text-align:center}

/* footer */
.footer{left:0;top:963px;width:1008px;height:166px;background:var(--footer)}
.footer h5{font-family:Arimo,Arial,sans-serif;font-size:9px;font-weight:700;color:#fff;text-transform:uppercase;position:absolute;top:33px}
.about-text{position:absolute;left:29px;top:55px;width:215px;font-size:9px;line-height:14px;color:#ccc}
.classes{position:absolute;left:279px;top:54px;list-style:none}
.classes li{font-size:9px;color:#ccc;line-height:16px;padding-left:12px;position:relative}
.classes li::before{content:"";position:absolute;left:0;top:5px;border-left:5px solid var(--red-bright);border-top:3px solid transparent;border-bottom:3px solid transparent}
.contact{position:absolute;left:532px;top:52px}
.contact div{display:flex;align-items:center;gap:9px;font-size:9px;color:#ccc;height:22px}
.social{position:absolute;left:773px;top:61px;display:flex;gap:11px}
.social span{width:20px;height:20px;border-radius:50%;background:#777}
.bottom{left:0;top:1129px;width:1008px;height:38px;background:var(--footer-bar)}
.bottom .copy{position:absolute;left:29px;top:14px;font-size:7px;color:#888}
.bottom .links{position:absolute;right:34px;top:13px;font-size:8px;color:#aaa}
.to-top{position:absolute;left:482px;top:-12px;width:38px;height:24px;border-radius:19px 19px 0 0;background:#111;display:flex;justify-content:center;align-items:center}
</style>
</head>
<body>
<div class="site">

  <header>
    <div class="abs brand"><span class="brand-mark"></span><span class="brand-name">IRON MARK TRAINING</span></div>
    <div class="abs tagline"><h2>STATE OF THE ART</h2><p>The most &nbsp;innovative training<br>&amp; Highest performance gear</p></div>
  </header>

  <nav class="abs nav">
    <a style="left:49px">Home</a>
    <a style="left:139px">About</a>
    <a style="left:230px">Classes</a>
    <a style="left:320px">Locations</a>
    <a style="left:434px">Store</a>
    <a style="left:526px">Range</a>
    <a class="register">Register</a>
  </nav>

  <section class="abs hero">
    <div class="hero-photo" role="img" aria-label="Shooter aiming a rifle on an indoor range, blurred blue background"></div>
    <div class="abs hero-copy">
      <h1>Why choose us ?</h1>
      <div class="rule"></div>
      <p>Your experience matters greatly to us. We pride ourselves on the service that comes with our knowledge and expertise</p>
    </div>
  </section>

  <article class="abs card retail">
    <div class="card-photo" role="img" aria-label="Close view of a pistol"></div>
    <h3 style="top:29px">PREMIUM RETAIL</h3>
    <p style="top:69px">The best firearms, accessories, and concealed carry lifestyle products. Carefully selected to give you every possible advantage.</p>
    <div class="btns" style="top:124px"><span class="btn btn-red">View retails</span><span class="btn btn-gray">Register for a class</span></div>
  </article>

  <article class="abs card staff">
    <div class="card-photo" role="img" aria-label="Instructor with shooter at a range lane"></div>
    <h3 style="top:29px">PROFESSIONAL STAFF</h3>
    <p style="top:69px;left:90px;right:90px">Friendly, knowledgeable, experienced and professional staff dedicated to helping you grow, improve, and learn as a shooter.</p>
    <div class="btns" style="top:124px"><span class="btn btn-red">Browse our staff</span><span class="btn btn-gray">Register for a class</span></div>
  </article>

  <article class="abs card tech">
    <div class="card-photo" role="img" aria-label="Virtual training room with table and chairs"></div>
    <h3 style="top:41px">INNOVATIVE TECHNOLOGY</h3>
    <p style="top:82px;left:80px;right:80px">Advanced and innovative virtual training systems that use actual firearms converted for completely safe and ultra realistic immersion.</p>
    <div class="btns" style="top:130px"><span class="btn btn-red">View retails</span><span class="btn btn-white">Register for a class</span></div>
  </article>

  <article class="abs card facility">
    <div class="card-photo" role="img" aria-label="Indoor range lanes with targets and ear protection"></div>
    <h3 style="top:54px;font-size:18px">PREMIER FACILITY</h3>
    <div class="btns" style="top:125px"><span class="btn btn-outline">State of fire range</span></div>
  </article>

  <article class="abs card experience">
    <div class="card-photo" role="img" aria-label="Range booth control panels"></div>
    <h3 style="top:54px;font-size:18px">EXPERIENCE</h3>
    <div class="btns" style="top:125px"><span class="btn btn-outline">Click to reserve</span></div>
  </article>

  <section class="abs newsletter">
    <h4>JOIN OUR NEWSLETTER</h4>
    <p>Lorem ipsum dolor sit amet, consectetuer adipiscing elitn ullamcorper.</p>
    <div class="news-field"></div>
    <div class="news-btn">SIGN UP</div>
  </section>

  <footer class="abs footer">
    <h5 style="left:29px">About us</h5>
    <p class="about-text">Lorem ipsum dolor sit amet, consectetuer adipiscing elit, sed diam nonummy nibha aliquam erat volutpat. Ut wisi enim ad minim veniam, quis nostrud exerci tation ullamcorper suscipit lobortis nisl ut aliquip ex ea commodo consequat.</p>

    <h5 style="left:279px">Train with us - classes</h5>
    <ul class="classes">
      <li>Conceal Carry</li>
      <li>Basic firearm introductions</li>
      <li>Women only</li>
      <li>Home defence</li>
      <li>Tactical defensive shooting</li>
    </ul>

    <h5 style="left:532px">Contact info</h5>
    <div class="contact">
      <div><svg width="10" height="12" viewBox="0 0 10 12"><path d="M5 0C2.2 0 0 2.2 0 4.8 0 8 5 12 5 12s5-4 5-7.2C10 2.2 7.8 0 5 0z" fill="#c0141c"/><circle cx="5" cy="4.7" r="1.7" fill="#1e1e1e"/></svg>Address: 123456 Exerci Tation Ullamcorper</div>
      <div><svg width="11" height="8" viewBox="0 0 11 8"><rect x=".5" y=".5" width="10" height="7" fill="none" stroke="#c0141c"/><path d="M.5.5l5 4 5-4" fill="none" stroke="#c0141c"/></svg>Email: info@yourcompany.com</div>
      <div><svg width="11" height="10" viewBox="0 0 11 10"><rect x="0" y="3" width="11" height="7" rx="1" fill="#c0141c"/><rect x="2" y="0" width="7" height="3" rx="1" fill="#c0141c"/><circle cx="5.5" cy="6.5" r="1.6" fill="#1e1e1e"/></svg>Phone: + 123 456 789,</div>
    </div>

    <h5 style="left:773px;top:35px">Follow us - social connections</h5>
    <div class="social"><span></span><span></span><span></span><span></span><span></span></div>
  </footer>

  <div class="abs bottom">
    <div class="to-top"><svg width="12" height="8" viewBox="0 0 12 8"><path d="M1 7l5-5 5 5" fill="none" stroke="#fff" stroke-width="2"/></svg></div>
    <span class="copy">COPYRIGHT © 2015 - ALL RIGHTS RESERVED</span>
    <span class="links">Home &nbsp;| &nbsp;About &nbsp;| &nbsp;Classes &nbsp;| &nbsp;Store &nbsp;| &nbsp;Rage</span>
  </div>

</div>
</body>
</html>
```